Business Card for Orvane Parts Wholesale supplier

Hi There! I need a new business card for our company. We are specialized in selling Orvane parts, mostly we sell new LCD screens for Telvox and Slatrons. I would like to see that back in the design.

You can find the colors and logo's on our website: www.dorvak-example.nl

Industry/Entity Type

Business

Contact Information for Business Card

My Details:
Lars Vintorp

Phone: 0031612873406
E-mail: Lars@dorvak-example.nl

Slogan: "Because Quality Matters"

Font styles to use
Sans Serif

Colors

Designer to choose colors to be used in the design.

Requirements
Must have
• A Black backside with the Dorvak logo on it. The front side should be clean with only my contact details.
• But I'm also open for something really different or awesome!
Nice to have
• Remember that we are in the parts & repairing industry, So i'll be handing those business cards mainly to repair companies. Maybe you can do something with that thought :)

```html
<!DOCTYPE html>
<html lang="en">
<head>
<meta charset="UTF-8">
<title>Dorvak Business Card</title>
<link rel="stylesheet" href="https://fonts.googleapis.com/css2?family=Open+Sans:wght@400;600;700&display=swap">
<style>
  :root {
    --stage: #e9e6e1;
    --card-black: #050505;
    --card-white: #f4f4f4;
    --brand-orange: #f29a2e;
    --brand-orange-deep: #e07f14;
    --ink-dark: #111111;
    --ink-light: #ffffff;
    --shadow: rgba(0, 0, 0, 0.22);
  }
  * { box-sizing: border-box; margin: 0; padding: 0; }
  html, body {
    width: 1200px;
    height: 780px;
    overflow: hidden;
    background: var(--stage);
    font-family: "Open Sans", Arial, sans-serif;
  }
  .stage {
    width: 1200px;
    height: 780px;
    display: flex;
    align-items: center;
    justify-content: center;
    gap: 40px;
  }
  .card {
    width: 540px;
    height: 309px;
    position: relative;
    overflow: hidden;
    box-shadow: 0 10px 28px var(--shadow);
  }

  /* Front side */
  .card-front { background: var(--card-black); }
  .front-top {
    position: absolute;
    left: 0; top: 0;
    width: 100%; height: 138px;
    background: var(--card-white);
    display: flex;
    align-items: center;
    padding-left: 44px;
  }
  .brand {
    display: flex;
    align-items: center;
    gap: 16px;
  }
  .brand-square {
    width: 54px; height: 54px;
    background: var(--brand-orange);
  }
  .brand-name {
    font-weight: 700;
    font-size: 64px;
    letter-spacing: -1px;
    line-height: 1;
    color: var(--ink-dark);
  }
  .front-band {
    position: absolute;
    left: 0; top: 138px;
    width: 100%; height: 34px;
    background: var(--brand-orange);
    display: flex;
    align-items: center;
    padding-left: 44px;
  }
  .holder-name {
    font-weight: 700;
    font-size: 19px;
    color: var(--ink-light);
  }
  .front-details {
    position: absolute;
    left: 44px; top: 184px;
    color: var(--ink-light);
  }
  .slogan-small {
    font-weight: 600;
    font-size: 16px;
    margin-bottom: 9px;
  }
  .contact-line {
    display: flex;
    align-items: center;
    gap: 10px;
    font-size: 15px;
    line-height: 1;
    margin-bottom: 7px;
  }
  .contact-icon {
    width: 18px; height: 18px;
    background: var(--brand-orange);
    display: flex;
    align-items: center;
    justify-content: center;
    flex-shrink: 0;
  }

  /* Back side */
  .card-back {
    background: var(--card-black);
    display: flex;
    flex-direction: column;
    align-items: center;
    justify-content: center;
  }
  .card-back .brand-name { color: var(--ink-light); font-size: 70px; }
  .card-back .brand-square { width: 58px; height: 58px; }
  .slogan-large {
    margin-top: 14px;
    font-size: 18px;
    color: var(--ink-light);
  }
</style>
</head>
<body>
  <main class="stage">
    <section class="card card-front" aria-label="Front of business card">
      <div class="front-top">
        <div class="brand">
          <div class="brand-square"></div>
          <span class="brand-name">Dorvak</span>
        </div>
      </div>
      <div class="front-band">
        <span class="holder-name">Lars Vintorp</span>
      </div>
      <div class="front-details">
        <p class="slogan-small">Because Quality Matters</p>
        <p class="contact-line">
          <span class="contact-icon">
            <svg width="12" height="12" viewBox="0 0 24 24" aria-hidden="true"><path fill="#050505" d="M6.6 10.8a15 15 0 0 0 6.6 6.6l2.2-2.2c.3-.3.7-.4 1-.2 1.1.4 2.3.6 3.6.6.6 0 1 .4 1 1V20c0 .6-.4 1-1 1A17 17 0 0 1 3 4c0-.6.4-1 1-1h3.5c.6 0 1 .4 1 1 0 1.3.2 2.5.6 3.6.1.3 0 .7-.2 1z"/></svg>
          </span>
          0031612873406
        </p>
        <p class="contact-line">
          <span class="contact-icon">
            <svg width="12" height="12" viewBox="0 0 24 24" aria-hidden="true"><rect x="2" y="5" width="20" height="14" fill="#050505"/><path d="M2 5l10 8 10-8" fill="none" stroke="#f29a2e" stroke-width="2"/></svg>
          </span>
          Lars@dorvak-example.nl
        </p>
        <p class="contact-line">
          <span class="contact-icon">
            <svg width="12" height="12" viewBox="0 0 24 24" aria-hidden="true"><circle cx="12" cy="12" r="9" fill="none" stroke="#050505" stroke-width="2"/><path d="M3 12h18M12 3c3 3 3 15 0 18M12 3c-3 3-3 15 0 18" fill="none" stroke="#050505" stroke-width="2"/></svg>
          </span>
          www.dorvak-example.nl
        </p>
      </div>
    </section>

    <section class="card card-back" aria-label="Back of business card">
      <div class="brand">
        <div class="brand-square"></div>
        <span class="brand-name">Dorvak</span>
      </div>
      <p class="slogan-large">Because Quality Matters</p>
    </section>
  </main>
</body>
</html>
```